Introducting Copley Sheetmetal MADE WITH PRIDE

We require a PDF fact sheet that we can share via email that has a summary of infomation, services and products as found on our website www.copleysheetmetal-example.com

The Call to Action - Heading should be "Made with Pride"

Needs to look professional, prefer sharp lines than bubble circles

Trying to attract new business

Target Market(s)

Potential new clients; Plumbers, Shop fitters, restaurants and Caters.

Industry/Entity Type

Manufacturing

Font styles to use
Other font styles liked:
• something masculine

Colors

Designer to choose colors to be used in the design.

Requirements
Must have
• Must be one page, low res so when emailing it's not too large.
• Must have phone number, email address and actual address
• Should include summary of copy from the website; www.copleysheetmetal-example.com
• * A bit about us
• * Services
• * Fabrication Range and Finishes
• * General Fabrication
Nice to have
• Something that is not too busy, easy to read - so not too much writing. Must look professional (that's why we using ArtHiveHub).
• Please let me know I you need images from the website and I'll sent to you.
Should not have
• It shouldn't be too busy, easy to read - so not too much writing. Simple and clear message.

```html
<!DOCTYPE html>
<html lang="en">
<head>
<meta charset="utf-8">
<title>Copley Sheetmetal – Made With Pride</title>
<link rel="stylesheet" href="https://fonts.googleapis.com/css2?family=Oswald:wght@700&family=Roboto:wght@400;500;700&family=Roboto+Condensed:wght@700&display=swap">
<style>
  :root {
    --page-bg: #e9e9e7;
    --slate: #3e4c5c;
    --panel-grey: #d5d7d8;
    --box-dark: #231f20;
    --ink: #1d1b1c;
    --white: #ffffff;
    --brand-slate: #3e4c5c;
  }
  html, body {
    margin: 0;
    padding: 0;
    width: 1200px;
    height: 966px;
    overflow: hidden;
    background: var(--page-bg);
  }
  .flyer {
    position: absolute;
    left: 280px;
    top: 30px;
    width: 640px;
    height: 906px;
    background: var(--slate);
    overflow: hidden;
    font-family: 'Roboto', Arial, sans-serif;
  }
  .intro-panel {
    position: absolute;
    left: 30px;
    top: 50px;
    width: 300px;
    height: 690px;
    background: var(--panel-grey);
    box-sizing: border-box;
    padding: 44px 22px 0 26px;
    color: var(--ink);
    overflow: hidden;
  }
  .brand {
    display: flex;
    align-items: center;
    gap: 10px;
    margin: 0 0 20px 10px;
  }
  .brand-square {
    width: 20px;
    height: 20px;
    background: var(--brand-slate);
    flex: none;
  }
  .brand-name {
    font-family: 'Roboto', Arial, sans-serif;
    font-weight: 700;
    font-size: 18px;
    letter-spacing: 1px;
    text-transform: uppercase;
    color: var(--brand-slate);
    white-space: nowrap;
  }
  .intro-copy {
    font-size: 16px;
    line-height: 1.3;
    margin: 0;
  }
  .headline {
    font-family: 'Oswald', 'Arial Narrow', sans-serif;
    font-weight: 700;
    font-size: 100px;
    line-height: 0.98;
    text-transform: uppercase;
    margin: 34px 0 0 0;
    letter-spacing: -1px;
  }
  .info-column {
    position: absolute;
    left: 345px;
    top: 34px;
    width: 270px;
    display: flex;
    flex-direction: column;
    gap: 14px;
  }
  .info-box {
    background: var(--box-dark);
    color: var(--white);
    box-sizing: border-box;
    padding: 12px 14px 13px 14px;
  }
  .info-box h2 {
    font-family: 'Roboto Condensed', 'Arial Narrow', sans-serif;
    font-weight: 700;
    font-size: 21px;
    line-height: 1.05;
    margin: 0 0 5px 0;
    text-transform: uppercase;
  }
  .info-box p {
    font-size: 13.5px;
    line-height: 1.3;
    margin: 0;
  }
  .contact {
    position: absolute;
    left: 34px;
    top: 770px;
    color: var(--white);
    font-size: 17px;
    line-height: 1.3;
    font-style: normal;
  }
  .contact .strong { font-weight: 700; }
  .photo-cluster {
    position: absolute;
    left: 340px;
    top: 652px;
    width: 300px;
    height: 254px;
  }
</style>
</head>
<body>
  <article class="flyer">
    <section class="intro-panel">
      <div class="brand">
        <span class="brand-square"></span>
        <span class="brand-name">Copley Sheetmetal</span>
      </div>
      <p class="intro-copy">Fast, friendly, and fully functional, our professional Metal Fabrication Service.<br>
      We provide general sheetmetal and light steel fabrication services (cutting, folding, mig/tig welding) working with stainless steel, copper, galvanised steel, aluminium and mild steel.</p>
      <h1 class="headline">Made<br>With<br>Pride</h1>
    </section>

    <div class="info-column">
      <section class="info-box box-services">
        <h2>Services</h2>
        <p>We can produce and supply a range of sheet metal components for all industries. We provide general sheetmetal &amp; light steel fabrication services (cutting, folding, mig/tig welding) working with stainless steel, aluminium, copper, galvanised steel &amp; mild steel.</p>
      </section>

      <section class="info-box box-facilities">
        <h2>Facilities, Materials<br>&amp; Finishes</h2>
        <p>We have an extensive range of equipment &amp; sheet metal machinery. We have experienced tradespeople with extensive experience &amp; abilities to custom fabricate to your specific design. Contact us now</p>
      </section>

      <section class="info-box box-general">
        <h2>General<br>Fabrication</h2>
        <p>Wether you're performing shop fabrication, repairing equipment on a farm or job site, or creating artwork in your garage, Copley Sheetmetal has the knowhow, creativity and process knowledge to help you get your job done right.</p>
      </section>
    </div>

    <address class="contact">
      48 Harcourt Rd, Kelvale<br>
      SA 5094, Australia<br>
      <span class="strong">(08) 5550 4188</span><br>
      <span class="strong">info@copleysheetmetal-example.com</span><br>
      <span class="strong">www.copleysheetmetal-example.com</span>
    </address>

    <svg class="photo-cluster" viewBox="0 0 300 254" width="300" height="254">
      <defs>
        <linearGradient id="coil-tone" x1="0" y1="0" x2="1" y2="1">
          <stop offset="0" stop-color="#c9ccce"/>
          <stop offset="1" stop-color="#6c6a66"/>
        </linearGradient>
        <linearGradient id="machine-tone" x1="0" y1="0" x2="1" y2="1">
          <stop offset="0" stop-color="#b9bcbf"/>
          <stop offset="1" stop-color="#2f5a9a"/>
        </linearGradient>
        <linearGradient id="welder-tone" x1="0" y1="0" x2="1" y2="1">
          <stop offset="0" stop-color="#8a5a45"/>
          <stop offset="1" stop-color="#3b3a3f"/>
        </linearGradient>
      </defs>
      <circle cx="262" cy="128" r="82" fill="url(#machine-tone)" stroke="#ffffff" stroke-width="6" role="img" aria-label="Photo of sheet metal folding machinery"/>
      <circle cx="150" cy="186" r="82" fill="url(#coil-tone)" stroke="#ffffff" stroke-width="6" role="img" aria-label="Photo of stacked steel coils"/>
      <circle cx="84" cy="80" r="74" fill="url(#welder-tone)" stroke="#ffffff" stroke-width="6" role="img" aria-label="Photo of a tradesperson welding in a hi-vis vest"/>
    </svg>
  </article>
</body>
</html>
```